We need a podcast cover design that will be used on Vexora. The podcast is called Founder Temperament Dial. The people we want to attract want us to be direct, real and upfront wiht them. They live in a noisy world and want clear and elegant design and funciton. We work with entrepreneurs who like brands like Quorla, Zentrix and Movari. We want a simple elegant design that uses the title on the cover along with the photo we uploaded. If someone goes to vexora, we want this to stand out and be visible.

Target Market(s)

Entrepreneurs, Artists, People who think differently

Industry/Entity Type

Consultant

Font styles to use
Sans Serif

Colors

Designer to choose colors to be used in the design.

Requirements
Must have
• The title on the podcast cover that will be legible on vExora. There should be high contrast so that the cover stands out on vexora with everyoe else.
Nice to have
• I would like to see the photo offset either right or left and bleeding off the page.
Should not have
• Too many colors, patterns or designs. Simple, elegant, and clean.

```html
<!DOCTYPE html>
<html lang="en">
<head>
<meta charset="utf-8">
<title>Founder Temperament Dial — Podcast Cover</title>
<link rel="stylesheet" href="https://fonts.googleapis.com/css2?family=Alfa+Slab+One&display=swap">
<style>
  :root {
    --sky-deep: #0a3fb8;
    --sky-mid: #1f7fe6;
    --sky-light: #5cc6f5;
    --ink-shadow: #0b1a3a;
    --title-white: #ffffff;
    --portrait-skin: #c98f6e;
    --portrait-shirt: #9fd0ea;
  }
  * { margin: 0; padding: 0; box-sizing: border-box; }
  html, body {
    width: 1200px;
    height: 1200px;
    overflow: hidden;
    background: var(--sky-deep);
  }
  .cover {
    position: relative;
    width: 1200px;
    height: 1200px;
    overflow: hidden;
  }
  .cover__backdrop {
    position: absolute;
    inset: 0;
    background:
      radial-gradient(ellipse 70% 55% at 42% 45%, var(--sky-light) 0%, var(--sky-mid) 45%, transparent 80%),
      linear-gradient(180deg, var(--sky-deep) 0%, var(--sky-mid) 55%, var(--sky-deep) 100%);
  }
  .cover__portrait {
    position: absolute;
    right: 0;
    top: 48px;
    width: 560px;
    height: 1152px;
    border-radius: 260px 0 0 0;
    background: linear-gradient(180deg, var(--portrait-skin) 0%, var(--portrait-skin) 58%, var(--portrait-shirt) 72%, var(--portrait-shirt) 100%);
  }
  .cover__title {
    position: absolute;
    left: 30px;
    top: 330px;
    width: 600px;
    text-align: center;
    font-family: "Alfa Slab One", serif;
    color: var(--title-white);
    line-height: 1;
    text-shadow: 3px 4px 4px var(--ink-shadow);
  }
  .cover__title-line {
    display: block;
    font-size: 150px;
    transform: scaleX(0.68);
    transform-origin: center;
    letter-spacing: -2px;
    margin-bottom: 42px;
  }
</style>
</head>
<body>
  <main class="cover">
    <div class="cover__backdrop" role="img" aria-label="Blue world map with silhouettes of business people shaking hands"></div>
    <div class="cover__portrait" role="img" aria-label="Portrait photo of the smiling host in a light blue t-shirt"></div>
    <h1 class="cover__title">
      <span class="cover__title-line">Founder</span>
      <span class="cover__title-line">Temperament</span>
      <span class="cover__title-line">Dial</span>
    </h1>
  </main>
</body>
</html>
```